10 Labels for Wild Bird Food

Label Design Request for New Products
We are excited to announce the launch of 10 new products and are seeking vibrant, fun, and colorful labels to match their energy. Each label should measure 6 x 4 inches (152.4mm x 101.6mm) and must feature our brand logo. Additionally, please include all the necessary information as detailed in the attached Word document.

Let's make our products stand out on the shelves with eye-catching designs!

Target Market(s)

Wild Bird Food Buyers

Requirements
Must have
• Logo

```html
<!DOCTYPE html>
<html lang="en">
<head>
<meta charset="utf-8">
<title>Busy Beaks – Niger Seed 5L Bag Label</title>
<link href="https://fonts.googleapis.com/css2?family=Outfit:wght@300;400;500;600;700&display=swap" rel="stylesheet">
<style>
  :root {
    --page: #ececec;
    --label: #f0efc8;
    --ink: #3b3b2d;
    --teal: #138b80;
    --green: #8bbb1c;
    --white: #ffffff;
  }
  * { box-sizing: border-box; margin: 0; padding: 0; }
  html, body {
    width: 1200px; height: 1200px; overflow: hidden;
    background: var(--page);
    font-family: "Outfit", sans-serif;
    color: var(--ink);
  }
  .label {
    position: absolute; left: 50px; top: 233px;
    width: 1100px; height: 733px;
    background: var(--label);
    border-radius: 52px;
    overflow: hidden;
  }
  .seed-photo {
    position: absolute; left: 330px; top: 175px;
    width: 420px; height: 470px;
    border-radius: 50%;
    background: radial-gradient(ellipse at center, rgba(150,155,110,0.45) 0%, rgba(170,172,125,0.25) 50%, rgba(240,239,200,0) 72%);
  }
  .brand {
    position: absolute; left: 0; right: 0; top: 78px;
    display: flex; justify-content: center; align-items: center; gap: 14px;
  }
  .brand-dot {
    width: 56px; height: 56px; border-radius: 50%;
    background: var(--teal);
  }
  .brand-name {
    font-weight: 700; font-size: 62px; line-height: 1;
    color: var(--teal); letter-spacing: 0.5px;
  }
  .product-title {
    position: absolute; left: 0; right: 0; top: 215px;
    text-align: center;
    font-weight: 600; font-size: 86px; line-height: 1;
    letter-spacing: 1px;
  }
  .copy {
    position: absolute; left: 67px; top: 337px; width: 530px;
  }
  .copy h2 {
    font-weight: 600; font-size: 19.5px; line-height: 24px;
    color: var(--teal); text-transform: uppercase; letter-spacing: 0.4px;
  }
  .copy p {
    font-weight: 300; font-size: 17px; line-height: 20.3px;
    letter-spacing: 0.15px;
    text-align: justify; margin-top: 4px;
  }
  .copy .usage { margin-top: 14px; }
  .net-weight {
    position: absolute; left: 632px; width: 396px; top: 341px;
    text-align: center; font-weight: 500; font-size: 17.5px;
  }
  .code-box {
    position: absolute; left: 632px; top: 371px;
    width: 396px; height: 163px;
    background: var(--white); border-radius: 21px;
  }
  .batch-box {
    position: absolute; left: 632px; top: 552px;
    width: 396px; height: 56px;
    background: var(--white); border-radius: 14px;
    display: flex; align-items: center; justify-content: center;
    font-size: 16.5px; letter-spacing: 0.4px;
  }
  .batch-box b { font-weight: 600; }
  .batch-box span { font-weight: 300; }
  .batch-box .sep { margin: 0 9px; font-weight: 300; }
  .notice {
    position: absolute; left: 632px; width: 396px; top: 611px;
    text-align: center; font-weight: 600; font-size: 11.2px;
  }
  .footer {
    position: absolute; left: 0; bottom: 0;
    width: 100%; height: 85px;
    background: var(--ink); color: var(--white);
  }
  .sku {
    position: absolute; left: 67px; top: 32px;
    font-size: 15px; font-weight: 500;
  }
  .contact {
    position: absolute; left: 0; right: 0; top: 26px;
    text-align: center; font-size: 13px; font-weight: 500; line-height: 18px;
  }
  .social {
    position: absolute; right: 61px; top: 26px;
    display: flex; gap: 4px;
  }
  .social span {
    width: 31px; height: 31px; border-radius: 50%;
    background: var(--white); display: block;
  }
</style>
</head>
<body>
  <main class="label">
    <div class="seed-photo" role="img" aria-label="Faint background photo of a pile of niger seeds"></div>

    <div class="brand">
      <span class="brand-dot"></span>
      <span class="brand-name">busy beaks</span>
    </div>

    <h1 class="product-title">Niger Seed 5L Bag</h1>

    <section class="copy">
      <h2>Attract a burst of color to your garden with nutritious niger seed!</h2>
      <p>Invite a beautiful array of small, colorful birds to your garden with our Niger Seed 5L Bag, the top choice for bird enthusiasts who want to provide their feathered friends with a nutrient-rich and highly desirable treat. Known for its appeal to finches and other small birds, this premium bird seed will make your garden a lively and vibrant bird haven.</p>
      <h2 class="usage">Easy to use:</h2>
      <p>Fill your nyjer seed feeders or sprinkle on bird tables to create an irresistible feast for your garden birds. Watch as they flock to your garden, bringing vibrant colors and cheerful chirping to your outdoor space.</p>
    </section>

    <div class="net-weight">Net Weight: 3300g</div>
    <div class="code-box"></div>
    <div class="batch-box">
      <b>EXPIRY DATE:</b>&nbsp;<span>00/000</span><span class="sep">|</span><b>BATCH:</b>&nbsp;<span>0000</span>
    </div>
    <div class="notice">Not for human consumption &nbsp;|&nbsp; May Contain Nuts</div>

    <footer class="footer">
      <div class="sku">BB26</div>
      <div class="contact">Marlow Trading, Oakridge Business Park, Haslemere, GU27 4XY<br>sales@marlowtrading.co.uk</div>
      <div class="social"><span></span><span></span><span></span></div>
    </footer>
  </main>
</body>
</html>
```